Bref créative
Thriving Neighbors of Alder Valley
Professional
This is a TEMPLATE for a card that will be used for many, many people, thus we need a design that allows us a template format that can be input with all the standard info, title, address, phone, cell, fax, email and web address.
Please use a template format that so that we can change card to various people

```html
<!DOCTYPE html>
<html lang="en">
<head>
<meta charset="utf-8">
<title>Thriving Neighbors of Alder Valley – Business Card Template</title>
<link rel="stylesheet" href="https://fonts.googleapis.com/css2?family=Open+Sans:wght@400;700;800&display=swap">
<style>
  :root {
    --backdrop: #ece9e4;
    --card-white: #ffffff;
    --green-deep: #1d7a1f;
    --green-bright: #3aa53a;
    --navy: #1f2a5a;
    --brand-green: #2f9b3a;
    --ink-light: #ffffff;
  }
  * { margin: 0; padding: 0; box-sizing: border-box; }
  html, body {
    width: 1200px; height: 852px; overflow: hidden;
    background: var(--backdrop);
    font-family: "Open Sans", Arial, sans-serif;
  }
  .canvas { position: relative; width: 1200px; height: 852px; }
  .card {
    position: absolute; width: 540px; height: 310px;
    background: var(--card-white); border-radius: 16px; overflow: hidden;
    box-shadow: 0 8px 22px rgba(0,0,0,0.18);
  }
  .card--front { left: 70px; top: 90px; }
  .card--back { left: 590px; top: 452px; }
  .card__wave { position: absolute; inset: 0; width: 100%; height: 100%; }
  .identity { position: absolute; color: var(--ink-light); }
  .identity__name { font-size: 19px; font-weight: 700; line-height: 1.2; }
  .identity__title { font-size: 13px; font-weight: 400; }
  .contact { position: absolute; color: var(--ink-light); font-size: 12.5px; line-height: 1.5; }
  .contact__address { margin-bottom: 10px; }
  .contact__row { display: flex; align-items: center; gap: 7px; }
  .contact__icon { width: 12px; height: 12px; flex: none; }
  .brand { position: absolute; display: flex; flex-direction: column; align-items: center; text-align: center; }
  .brand__mark { width: 34px; height: 34px; background: var(--navy); margin-bottom: 12px; }
  .brand__name { font-size: 19px; font-weight: 800; color: var(--brand-green); line-height: 1.15; }

  .card--front .identity { left: 26px; top: 30px; }
  .card--front .contact { left: 26px; top: 186px; }
  .card--front .brand { left: 290px; top: 88px; width: 220px; }

  .card--back .identity { right: 26px; top: 30px; text-align: right; }
  .card--back .contact { right: 26px; top: 170px; text-align: right; }
  .card--back .contact__row { justify-content: flex-end; }
  .card--back .brand { left: 24px; top: 100px; width: 220px; }
</style>
</head>
<body>
<main class="canvas">

  <article class="card card--front">
    <svg class="card__wave" viewBox="0 0 540 310" preserveAspectRatio="none" aria-hidden="true">
      <defs>
        <radialGradient id="greenFront" cx="30%" cy="55%" r="75%">
          <stop offset="0" stop-color="var(--green-bright)"/>
          <stop offset="1" stop-color="var(--green-deep)"/>
        </radialGradient>
      </defs>
      <path d="M0 0 H262 C196 92 196 200 300 310 H0 Z" fill="url(#greenFront)"/>
      <path d="M268 0 C204 92 206 200 312 310" fill="none" stroke="var(--navy)" stroke-width="5"/>
    </svg>
    <div class="identity">
      <p class="identity__name">Your name</p>
      <p class="identity__title">Job Title</p>
    </div>
    <div class="contact">
      <p class="contact__address">Suite 102 Street name,<br>State, Zip 2034,Country</p>
      <p class="contact__row">
        <svg class="contact__icon" viewBox="0 0 12 12"><path d="M2 1 L4.5 1 L5.5 3.5 L4 4.7 C4.8 6.4 5.6 7.2 7.3 8 L8.5 6.5 L11 7.5 L11 10 C6 10.5 1.5 6 2 1 Z" fill="currentColor"/></svg>
        127 345 9876
      </p>
      <p class="contact__row">
        <svg class="contact__icon" viewBox="0 0 12 12"><rect x="3" y="0.5" width="6" height="11" rx="1.2" fill="currentColor"/><rect x="4" y="2" width="4" height="6" fill="var(--green-deep)"/></svg>
        345 345 9876
      </p>
      <p class="contact__row">
        <svg class="contact__icon" viewBox="0 0 12 12"><circle cx="6" cy="6" r="5" fill="none" stroke="currentColor" stroke-width="1.4"/><circle cx="6" cy="6" r="2" fill="none" stroke="currentColor" stroke-width="1.4"/></svg>
        support@aldervalley.org
      </p>
    </div>
    <div class="brand">
      <span class="brand__mark"></span>
      <p class="brand__name">Thriving Neighbors<br>of Alder Valley</p>
    </div>
  </article>

  <article class="card card--back">
    <svg class="card__wave" viewBox="0 0 540 310" preserveAspectRatio="none" aria-hidden="true">
      <defs>
        <radialGradient id="greenBack" cx="70%" cy="55%" r="75%">
          <stop offset="0" stop-color="var(--green-bright)"/>
          <stop offset="1" stop-color="var(--green-deep)"/>
        </radialGradient>
      </defs>
      <path d="M540 0 H252 C318 92 318 200 214 310 H540 Z" fill="url(#greenBack)"/>
      <path d="M246 0 C310 92 308 200 202 310" fill="none" stroke="var(--navy)" stroke-width="5"/>
    </svg>
    <div class="identity">
      <p class="identity__name">Your name</p>
      <p class="identity__title">Job Title</p>
    </div>
    <div class="contact">
      <p class="contact__address">Suite 102 Street name,<br>State, Zip 2034,Country</p>
      <p class="contact__row">
        127 345 9876
        <svg class="contact__icon" viewBox="0 0 12 12"><path d="M2 1 L4.5 1 L5.5 3.5 L4 4.7 C4.8 6.4 5.6 7.2 7.3 8 L8.5 6.5 L11 7.5 L11 10 C6 10.5 1.5 6 2 1 Z" fill="currentColor"/></svg>
      </p>
      <p class="contact__row">
        345 345 9876
        <svg class="contact__icon" viewBox="0 0 12 12"><rect x="3" y="0.5" width="6" height="11" rx="1.2" fill="currentColor"/><rect x="4" y="2" width="4" height="6" fill="var(--green-deep)"/></svg>
      </p>
      <p class="contact__row">
        support@aldervalley.org
        <svg class="contact__icon" viewBox="0 0 12 12"><circle cx="6" cy="6" r="5" fill="none" stroke="currentColor" stroke-width="1.4"/><circle cx="6" cy="6" r="2" fill="none" stroke="currentColor" stroke-width="1.4"/></svg>
      </p>
    </div>
    <div class="brand">
      <span class="brand__mark"></span>
      <p class="brand__name">Thriving Neighbors<br>of Alder Valley</p>
    </div>
  </article>

</main>
</body>
</html>
```